Website for Apartment Rental in Prague

I would like to create designs of my website focused on luxury apartment rentals in Prague, Czech Republic. I created initial mock-ups, They are all attached. I need to design homepage and subpage. The mock-ups were created by combining elements from different websites that I liked but I need you to create a design that is unique and original. The attached files a only a guidance for the structure of the website but not for the design. Try to be creative.

Industry/Entity Type

Apartment

```html
<!DOCTYPE html>
<html lang="en">
<head>
<meta charset="utf-8">
<title>About Us – Prague Apartments</title>
<link rel="stylesheet" href="https://fonts.googleapis.com/css2?family=Montserrat:wght@400;500;600&family=Open+Sans:wght@400;600&family=Raleway:wght@400;500&display=swap">
<style>
:root{
  --bg-soft:#f5f4f4;
  --white:#ffffff;
  --taupe:#a08073;
  --taupe-dark:#8f6f62;
  --yellow:#e0d12e;
  --heading:#6b6b6b;
  --text:#8e8e8e;
  --title:#5c5c5c;
  --rule:#dedede;
  --faded:#e4e4e4;
  --card-empty:#eeeeee;
}
*{margin:0;padding:0;box-sizing:border-box}
html,body{width:1200px;height:946px;overflow:hidden}
body{position:relative;background:var(--white);font-family:"Open Sans",sans-serif;color:var(--text)}
.abs{position:absolute}

.about{position:absolute;left:0;top:0;width:1200px;height:428px;background:var(--bg-soft);border-top:2px solid #e9ecf2}
.section-title{position:absolute;left:0;width:1200px;text-align:center;font-family:"Montserrat",sans-serif;font-weight:500;font-size:22px;letter-spacing:1px;color:var(--heading)}
.rule{position:absolute;height:3px;border-top:1px solid var(--rule);border-bottom:1px solid var(--rule)}
.intro{position:absolute;left:290px;width:620px;text-align:center;font-size:9.6px;line-height:12px;color:var(--text)}

.feature{position:absolute;width:200px}
.feature h3{font-family:"Montserrat",sans-serif;font-weight:500;font-size:10.6px;color:var(--title);margin-bottom:5px;letter-spacing:.3px}
.feature p{font-size:9px;line-height:12px;color:var(--text)}
.feature.left{text-align:right}
.feature h3.accent{color:var(--taupe)}
.icon-badge{position:absolute;width:50px;height:50px;border-radius:50%;background:var(--white);border:1px solid #ececec;display:flex;align-items:center;justify-content:center}
.icon-badge.active{background:var(--yellow);border-color:var(--yellow)}
.hero-photo{position:absolute;left:496px;top:164px;width:208px;height:208px;border-radius:50%;
  background:linear-gradient(180deg,#d9d4ce 0%,#6b4d3a 22%,#3e2a20 45%,#2a4a4e 62%,#2e6b70 82%,#1f4c52 100%)}

.cta-band{position:absolute;left:0;top:428px;width:1200px;height:74px;background:var(--taupe)}
.cta-band p{position:absolute;left:297px;top:27px;font-family:"Raleway",sans-serif;font-size:15.5px;color:var(--white);letter-spacing:.4px}
.cta-button{position:absolute;left:797px;top:452px;width:106px;height:25px;background:var(--yellow);border:2px solid var(--white);color:var(--white);font-family:"Montserrat",sans-serif;font-weight:600;font-size:7px;letter-spacing:.5px;display:flex;align-items:center;justify-content:center}

.arrow{position:absolute;top:549px;width:12px;height:12px;background:var(--taupe);display:flex;align-items:center;justify-content:center}

.agent{position:absolute;top:631px;width:169px;height:268px;background:var(--white);border:1px solid #e6e6e6;border-top:none}
.agent .photo{position:absolute;left:-1px;top:0;width:169px;height:220px;background:linear-gradient(160deg,#4a3b33 0%,#2a2320 55%,#111 100%)}
.agent .photo.warm{background:linear-gradient(160deg,#3a2a26 0%,#8a6a5a 45%,#5a2a2a 100%)}
.agent .photo.empty{background:var(--card-empty)}
.agent h4{position:absolute;left:0;width:167px;top:230px;text-align:center;font-family:"Montserrat",sans-serif;font-weight:500;font-size:12.5px;color:var(--title)}
.agent .role{position:absolute;left:0;width:167px;top:250px;text-align:center;font-family:"Montserrat",sans-serif;font-size:8.6px;color:var(--text)}
.agent.faded{border-color:#f3f3f3}
.agent.faded h4,.agent.faded .role{color:var(--faded)}
.agent.highlight{border-bottom:2px solid var(--taupe)}
.agent.highlight h4{color:var(--taupe)}
.overlay{position:absolute;left:-1px;top:0;width:169px;height:220px;background:linear-gradient(160deg,#b0948a,#9a7a6c)}
.overlay .frame{position:absolute;left:10px;top:10px;width:149px;height:200px;border:1px solid rgba(255,255,255,.35)}
.overlay .phone{position:absolute;top:96px;width:169px;text-align:center;font-family:"Montserrat",sans-serif;font-weight:600;font-size:9.6px;color:var(--white)}
.overlay .email{position:absolute;top:115px;width:169px;text-align:center;font-family:"Montserrat",sans-serif;font-size:8px;color:var(--white)}
.overlay .socials{position:absolute;top:138px;width:169px;display:flex;justify-content:center;gap:20px}
.overlay .socials span{width:5px;height:5px;border-radius:50%;background:var(--white)}
.overlay .more{position:absolute;left:50px;top:183px;width:69px;height:19px;border:1px solid var(--white);color:var(--white);font-family:"Montserrat",sans-serif;font-size:6.6px;display:flex;align-items:center;justify-content:center;letter-spacing:.3px}
.bottom-rule{position:absolute;left:0;top:943px;width:1200px;height:2px;background:#eceef2}
</style>
</head>
<body>

<section class="about">
  <h2 class="section-title" style="top:38px">ABOUT US</h2>
  <div class="rule" style="left:234px;top:51px;width:286px"></div>
  <div class="rule" style="left:678px;top:51px;width:287px"></div>
  <p class="intro" style="top:76px">Aliquam dui justo, feugiat eu ligula at, posuere cursus enim. Fusce dictum egestas sem eu convallis. Suspendisse sapien turpis, iaculis eu congue at, tristique facilisis sapien. Vivamus sit amet cursus orci. Duis tempor vitae felis sed volutpat. Pellentesque quis leo turpis. Duis vestibulum euismod metus, ut iaculis tortor feugiat vel.</p>

  <div class="feature left" style="left:219px;top:150px">
    <h3 class="accent">Guidance</h3>
    <p>Sed turpis mi, porttitor nec congue<br>tempus, posuere nec sapien.<br>Mauris laoreet pellentesque justo.</p>
  </div>
  <div class="icon-badge active" style="left:431px;top:153px">
    <svg width="24" height="20" viewBox="0 0 24 20"><path d="M12 4 C9 2 5 2 2 3 V17 C5 16 9 16 12 18 C15 16 19 16 22 17 V3 C19 2 15 2 12 4Z" fill="#fff"/><path d="M12 4 V18" stroke="#e0d12e" stroke-width="1.4"/></svg>
  </div>

  <div class="feature left" style="left:190px;top:240px">
    <h3>Reputation</h3>
    <p>Aliquam dui justo, feugiat eu ligula<br>at, posuere cursus enim. Fusce<br>dictum egestas sem eu convallis.</p>
  </div>
  <div class="icon-badge" style="left:402px;top:243px">
    <svg width="24" height="22" viewBox="0 0 24 22"><rect x="2" y="9" width="5" height="11" fill="#a08073"/><path d="M8 9 L12 3 C13 1 15 2 14.5 4 L13.5 8 H20 C22 8 22.5 10 21.5 11 C22.5 12 22 13.5 21 14 C21.8 15 21.2 16.5 20 17 C20.5 18.5 19.5 20 18 20 H8Z" fill="#a08073"/></svg>
  </div>

  <div class="feature left" style="left:219px;top:330px">
    <h3>Happy Clients</h3>
    <p>Curabitur non mi id elit vestibulum<br>posuere. Nunc in risus arcu.<br>Quisque quis risus vitae augue</p>
  </div>
  <div class="icon-badge" style="left:431px;top:333px">
    <svg width="24" height="22" viewBox="0 0 24 22"><path d="M2 10 L12 2 L22 10 V20 H2Z" fill="none" stroke="#a08073" stroke-width="1.8"/><circle cx="9" cy="12" r="2" fill="#a08073"/><circle cx="15" cy="12" r="2" fill="#a08073"/><rect x="7" y="14.5" width="4" height="5.5" fill="#a08073"/><rect x="13" y="14.5" width="4" height="5.5" fill="#a08073"/></svg>
  </div>

  <div class="hero-photo" role="img" aria-label="Photo of a timber holiday house with a lit pool in front at dusk"></div>

  <div class="icon-badge" style="left:718px;top:153px">
    <svg width="20" height="24" viewBox="0 0 20 24"><rect x="2" y="2" width="16" height="20" fill="none" stroke="#a08073" stroke-width="1.6"/><path d="M5 7 H7 M9 7 H15 M5 11 H7 M9 11 H15 M5 15 H7 M9 15 H15 M5 19 H7 M9 19 H13" stroke="#a08073" stroke-width="1.4"/></svg>
  </div>
  <div class="feature" style="left:781px;top:150px">
    <h3>Listing</h3>
    <p>Phasellus tincidunt augue id nulla<br>bibendum, non efficitur ante<br>placerat. Donec tortor eros, congue</p>
  </div>

  <div class="icon-badge" style="left:746px;top:243px">
    <svg width="26" height="26" viewBox="0 0 26 26"><circle cx="12" cy="14" r="9" fill="none" stroke="#a08073" stroke-width="1.6"/><circle cx="12" cy="14" r="5.5" fill="none" stroke="#a08073" stroke-width="1.6"/><circle cx="12" cy="14" r="2" fill="#a08073"/><path d="M12 14 L22 6 M19 4 L22 6 L24 9" stroke="#a08073" stroke-width="1.6" fill="none"/></svg>
  </div>
  <div class="feature" style="left:808px;top:240px">
    <h3>Advertise</h3>
    <p>Aliquam risus mauris, congue sed<br>suscipit in, tincidunt euismod leo.<br>Etiam dolor diam, aliquet ut ante id,</p>
  </div>

  <div class="icon-badge" style="left:718px;top:333px">
    <svg width="26" height="24" viewBox="0 0 26 24"><path d="M13 12 L4 7 M13 12 L21 4 M13 12 L23 14 M13 12 L8 21 M13 12 L17 21" stroke="#a08073" stroke-width="1.4"/><circle cx="13" cy="12" r="3.5" fill="#a08073"/><circle cx="4" cy="7" r="2" fill="#a08073"/><circle cx="21" cy="4" r="2" fill="#a08073"/><circle cx="23" cy="14" r="2" fill="#a08073"/><circle cx="8" cy="21" r="2" fill="#a08073"/><circle cx="17" cy="21" r="2" fill="#a08073"/></svg>
  </div>
  <div class="feature" style="left:781px;top:330px">
    <h3>Consulting</h3>
    <p>Cras neque turpis, dictum at<br>tempus a, dapibus sit amet tortor.<br>Interdum et malesuada fames ac</p>
  </div>
</section>

<section class="cta-band">
  <p>Vivamus sapien augue, tempus ut ipsum id, molestie pulvinar ex.</p>
</section>
<a class="cta-button">CONTACT US</a>

<section class="agents">
  <h2 class="section-title" style="top:541px">OUR AGENTS</h2>
  <div class="rule" style="left:234px;top:554px;width:240px"></div>
  <div class="rule" style="left:725px;top:554px;width:240px"></div>
  <span class="arrow" style="left:492px"><svg width="6" height="8" viewBox="0 0 6 8"><path d="M5 1 L2 4 L5 7" stroke="#fff" stroke-width="1.4" fill="none"/></svg></span>
  <span class="arrow" style="left:696px"><svg width="6" height="8" viewBox="0 0 6 8"><path d="M1 1 L4 4 L1 7" stroke="#fff" stroke-width="1.4" fill="none"/></svg></span>
  <p class="intro" style="top:579px">Aliquam dui justo, feugiat eu ligula at, posuere cursus enim. Fusce dictum egestas sem eu convallis.<br>Suspendisse sapien turpis, iaculis eu congue at, tristique facilisis sapien.</p>

  <div class="agent faded" style="left:47px">
    <div class="photo empty" role="img" aria-label="Agent portrait placeholder"></div>
    <h4>Oliver Hartley</h4><div class="role">Senior Agent</div>
  </div>
  <div class="agent" style="left:234px">
    <div class="photo" role="img" aria-label="Portrait photo of agent Martin Sedlak"></div>
    <h4>Martin Sedlak</h4><div class="role">Senior Agent</div>
  </div>
  <div class="agent" style="left:422px">
    <div class="photo warm" role="img" aria-label="Portrait photo of agent Klara Dvorak"></div>
    <h4>Klara Dvorak</h4><div class="role">Senior Agent</div>
  </div>
  <div class="agent highlight" style="left:610px">
    <div class="overlay" role="img" aria-label="Portrait photo of agent Pavel Marek under a contact overlay">
      <div class="frame"></div>
      <div class="phone">(420)-555-0187</div>
      <div class="email">pavel.marek@example.com</div>
      <div class="socials"><span></span><span></span><span></span></div>
      <div class="more">MORE INFO</div>
    </div>
    <h4>Pavel Marek</h4><div class="role">Senior Agent</div>
  </div>
  <div class="agent" style="left:797px">
    <div class="photo" role="img" aria-label="Portrait photo of agent Lukas Brandt"></div>
    <h4>Lukas Brandt</h4><div class="role">Senior Agent</div>
  </div>
  <div class="agent faded" style="left:984px">
    <div class="photo empty" role="img" aria-label="Agent portrait placeholder"></div>
    <h4>Eliska Horak</h4><div class="role">Senior Agent</div>
  </div>
</section>
<div class="bottom-rule"></div>

</body>
</html>
```